"Psychic / Tarot Card Reader / Healer Needs a Web Page Design

We need a web page design for company that does psychic / tarot card readings / healings etc.
It currently has 6 different tabs which include: Home, testimonials, service, certificates, contact us plus a shop where if people want to they can purchase services on line.
Should be mystical / magic like yet simple.
Will upload a copy of the current logo for the business.
It's name is Velvet Lantern.

Target Market(s)

spiritual

Industry/Entity Type

It Company

Number of Pages Required

5+ page

```html
<!DOCTYPE html>
<html lang="en">
<head>
<meta charset="utf-8">
<title>Velvet Lantern</title>
<link href="https://fonts.googleapis.com/css2?family=Cormorant+Garamond:ital,wght@1,500;1,600&family=Tinos:wght@400;700&display=swap" rel="stylesheet">
<style>
:root{
  --plum:#7b1f86;
  --plum-deep:#3a0f5c;
  --night:#150c3a;
  --violet:#5d1a80;
  --yellow:#f6ec0c;
  --mint:#6fbf8f;
  --mint-light:#a8e0b8;
  --mustard:#d6cf32;
  --ink:#222;
  --body:#333;
  --white:#fff;
  --line:#d8d0e0;
}
*{box-sizing:border-box;margin:0;padding:0}
html,body{width:1200px;height:2332px;overflow:hidden;background:var(--white)}
body{position:relative;font-family:"Tinos",serif;color:var(--body)}
.script{font-family:"Cormorant Garamond",serif;font-style:italic;font-weight:600}
a{color:inherit;text-decoration:none}

/* header */
.site-header{position:absolute;left:0;top:0;width:1200px;height:117px;background:var(--white)}
.brand{position:absolute;left:162px;top:30px;font-family:"Cormorant Garamond",serif;font-style:italic;font-weight:600;font-size:34px;color:var(--plum);line-height:1}
.brand.footer-brand{left:162px;top:2090px;color:var(--white);font-size:32px}
.social{position:absolute;left:910px;top:20px;display:flex;gap:9px}
.social span{width:27px;height:27px;border-radius:50%;background:var(--plum)}
.main-nav{position:absolute;top:70px;left:0;width:1200px;height:30px}
.main-nav a{position:absolute;font-family:"Cormorant Garamond",serif;font-style:italic;font-weight:600;font-size:22px;color:var(--ink)}
.main-nav a.current{color:var(--plum)}

/* hero */
.hero{position:absolute;left:0;top:117px;width:1200px;height:542px;
  background:radial-gradient(ellipse at 75% 40%,#4a1f7a 0%,#2a1455 45%,#170b3b 80%)}
.hero-photo{position:absolute;left:0;top:0;width:470px;height:542px;
  background:linear-gradient(160deg,#1b1b22 0%,#3b2a2a 45%,#c9a38e 80%,#e6cfc3 100%);opacity:.9}
.hero-title{position:absolute;right:162px;top:150px;font-size:68px;color:var(--yellow);line-height:1}
.hero-text{position:absolute;right:162px;top:256px;width:420px;text-align:right;font-size:20px;line-height:29px;color:var(--white)}
.ribbon{position:absolute;display:flex;align-items:center;justify-content:center;font-family:"Cormorant Garamond",serif;font-style:italic;font-weight:600;color:var(--ink);
  clip-path:polygon(0 0,100% 0,100% 100%,0 100%,14% 50%)}
.hero .ribbon{left:912px;top:362px;width:126px;height:39px;background:var(--yellow);font-size:19px;padding-left:16px}
.dots{position:absolute;left:560px;top:492px;display:flex;gap:5px}
.dots span{width:15px;height:15px;border-radius:50%;background:#8a8699}
.dots span.on{background:var(--white)}

/* welcome */
.welcome{position:absolute;left:0;top:659px;width:1200px;height:278px}
.welcome h1{position:absolute;left:0;top:52px;width:1200px;text-align:center;font-size:44px;color:var(--ink);font-weight:500}
.welcome p{position:absolute;left:208px;top:140px;width:784px;text-align:center;font-size:14px;line-height:25px;color:var(--body)}

/* services */
.services{position:absolute;left:0;top:937px;width:1200px;height:568px;
  background:radial-gradient(ellipse at 50% 50%,#3a1f6e 0%,#1b0f45 55%,#0f0830 100%)}
.services::before,.services::after{content:"";position:absolute;left:0;width:1200px;height:7px;background:var(--line)}
.services::before{top:0}.services::after{bottom:0}
.card{position:absolute;top:101px;width:279px;height:372px}
.card-photo{height:162px}
.card h2{position:absolute;left:20px;top:186px;font-size:32px;color:var(--white);font-weight:500}
.card p{position:absolute;left:20px;top:236px;width:240px;font-size:13px;line-height:20px;color:var(--white)}
.card .ribbon{left:0;top:310px;width:124px;height:39px;font-size:16px;clip-path:polygon(0 0,100% 0,86% 50%,100% 100%,0 100%)}
.card.psychic{left:162px;background:var(--plum)}
.card.psychic .card-photo{background:linear-gradient(135deg,#6b4a3f,#c49282,#8f5a4e)}
.card.psychic .ribbon{background:var(--mint-light)}
.card.healer{left:460px;background:var(--mint)}
.card.healer .card-photo{background:radial-gradient(circle at 50% 40%,#f3e2c6,#a77fa8 55%,#4f6a5a)}
.card.healer .ribbon{background:var(--yellow)}
.card.reader{left:758px;width:280px;background:var(--mustard)}
.card.reader .card-photo{background:linear-gradient(135deg,#d9c88a,#c5a35a,#8f8a6a)}
.card.reader .ribbon{background:var(--plum);color:var(--white)}

/* media + video */
.section-title{position:absolute;top:1568px;font-size:36px;color:var(--ink);font-weight:500}
.media-item{position:absolute;left:162px;width:380px;height:80px}
.date-box{position:absolute;left:0;top:0;width:62px;height:75px;border:1px solid var(--line)}
.date-box .day{display:block;height:38px;background:var(--plum);color:var(--white);font-size:13px;text-align:center;line-height:38px}
.date-box .date{display:block;text-align:center;font-family:"Cormorant Garamond",serif;font-style:italic;font-weight:600;font-size:14px;line-height:35px;color:var(--plum)}
.media-item h3{position:absolute;left:84px;top:-4px;font-size:18px;color:var(--plum);font-weight:600;white-space:nowrap}
.media-item p{position:absolute;left:84px;top:22px;width:295px;font-size:12.5px;line-height:20px;color:var(--body)}
.video{position:absolute;left:614px;top:1640px;width:424px;height:295px;
  background:linear-gradient(120deg,#8a3f8a 0%,#c4672f 25%,#2b2b55 50%,#111 70%,#6d4fa0 100%)}
.video svg{position:absolute;left:182px;top:117px}

/* footer */
.site-footer{position:absolute;left:0;top:2018px;width:1200px;height:314px;
  background:linear-gradient(180deg,#241046 0%,#36155f 45%,#5b1c8c 80%,#7a2aa8 100%)}
.contact{position:absolute;left:162px;top:174px;font-size:12px;line-height:19px;color:var(--white)}
.f-col{position:absolute;top:50px}
.f-col h4{font-family:"Cormorant Garamond",serif;font-style:italic;font-weight:600;font-size:20px;color:var(--yellow);margin-bottom:10px}
.f-col li{list-style:none;font-size:12px;line-height:21px;color:var(--white)}
.newsletter .field{width:185px;height:34px;background:var(--white);margin-bottom:7px;padding-left:8px;font-family:"Cormorant Garamond",serif;font-style:italic;font-weight:600;font-size:13px;line-height:34px;color:var(--ink)}
.newsletter .signup{width:185px;height:34px;background:var(--yellow);text-align:center;font-family:"Cormorant Garamond",serif;font-style:italic;font-weight:600;font-size:20px;line-height:34px;color:var(--ink)}
.footer-rule{position:absolute;left:162px;top:244px;width:876px;height:1px;background:rgba(255,255,255,.2)}
.copyright{position:absolute;left:0;top:266px;width:1200px;text-align:center;font-size:12px;color:var(--white)}
</style>
</head>
<body>

<header class="site-header">
  <div class="brand">Velvet Lantern</div>
  <div class="social" aria-label="Social links"><span></span><span></span><span></span><span></span></div>
  <nav class="main-nav">
    <a class="current" style="left:441px">Home</a>
    <a style="left:532px">Testimonials</a>
    <a style="left:670px">Service</a>
    <a style="left:765px">Certificates</a>
    <a style="left:895px">Contact</a>
    <a style="left:996px">Shop</a>
  </nav>
</header>

<section class="hero">
  <div class="hero-photo" role="img" aria-label="Hand holding a fan of tarot cards"></div>
  <h1 class="hero-title script">Velvet Lantern</h1>
  <p class="hero-text">Maren has undertaken various training courses to give herself an indepth knowledge and understanding of Tarot and Reiki.</p>
  <a class="ribbon">Read More</a>
  <div class="dots"><span></span><span></span><span></span><span class="on"></span><span></span></div>
</section>

<section class="welcome">
  <h1 class="script">Welcome To Velvet Lantern</h1>
  <p>Maren has undertaken various training courses to give herself an indepth knowledge and understanding of Tarot and Reiki whilst applying her intution to provide her clients with indepth readings. She aims to offer clients guidance and support in any area of their life through the use of these methods. When providing Readings and Reiki Healings, Maren will use her skills and intuition to pass on accurate messages to clients from Heavenly Beings who wish their words and advice to become heard.</p>
</section>

<section class="services">
  <article class="card psychic">
    <div class="card-photo" role="img" aria-label="Open palm above crystals and cards"></div>
    <h2 class="script">Psychic</h2>
    <p>Sut perspiciatis unde omnis iste natus error sit voluem ustium doloremque laudantium, totam rem aperiamaeipsa e ab illo in</p>
    <a class="ribbon">Read More</a>
  </article>
  <article class="card healer">
    <div class="card-photo" role="img" aria-label="Two hands raised in glowing light"></div>
    <h2 class="script">Healer</h2>
    <p>Sut perspiciatis unde omnis iste natus error sit voluem ustium doloremque laudantium, totam rem aperiamaeipsa e ab illo in</p>
    <a class="ribbon">Read More</a>
  </article>
  <article class="card reader">
    <div class="card-photo" role="img" aria-label="Spread of tarot cards on a table"></div>
    <h2 class="script">Tarot Card Reader</h2>
    <p>Sut perspiciatis unde omnis iste natus error sit voluem ustium doloremque laudantium, totam rem aperiamaeipsa e ab illo in</p>
    <a class="ribbon">Read More</a>
  </article>
</section>

<h2 class="section-title script" style="left:162px">In the Media</h2>
<h2 class="section-title script" style="left:614px">Our Video</h2>

<div class="media-item" style="top:1641px">
  <div class="date-box"><span class="day">Today</span><span class="date">Mar,02</span></div>
  <h3 class="script">Celeste Arbor and Rowan Vale</h3>
  <p>Sut perspiciatis unde omnis iste natus error sit voluem ustium doloremque laudantium, totam rem aperiamae ipsa e ab illo inventore veritatis.</p>
</div>
<div class="media-item" style="top:1750px">
  <div class="date-box"><span class="day">Today</span><span class="date">Mar,02</span></div>
  <h3 class="script">Advanced Angel Practitioner</h3>
  <p>Sut perspiciatis unde omnis iste natus error sit voluem ustium doloremque laudantium, totam rem aperiamae ipsa e ab illo inventore veritatis.</p>
</div>
<div class="media-item" style="top:1860px">
  <div class="date-box"><span class="day">Today</span><span class="date">Mar,02</span></div>
  <h3 class="script">Reiki Masters - Elias Thorne</h3>
  <p>Sut perspiciatis unde omnis iste natus error sit voluem ustium doloremque laudantium, totam rem aperiamae ipsa e ab illo inventore veritatis.</p>
</div>

<div class="video" role="img" aria-label="Video still of tarot cards on a patterned cloth">
  <svg width="60" height="60" viewBox="0 0 60 60" aria-hidden="true">
    <circle cx="30" cy="30" r="27" fill="none" stroke="#fff" stroke-width="3"/>
    <path d="M24 18 L42 30 L24 42 Z" fill="none" stroke="#fff" stroke-width="3" stroke-linejoin="round"/>
  </svg>
</div>

<footer class="site-footer">
  <div class="brand footer-brand" style="top:72px">Velvet Lantern</div>
  <div class="contact">Phone: 0400 555 217<br>Email:&nbsp; maren@velvetlantern.example</div>
  <div class="f-col" style="left:384px">
    <h4>What We Do</h4>
    <ul><li>Advanced Angel</li><li>Tarot Course</li><li>Certified Realm Reader</li><li>Reiki Masters</li><li>Dream Interpretatioin</li><li>Spiral Dance</li></ul>
  </div>
  <div class="f-col" style="left:572px">
    <h4>Links</h4>
    <ul><li>Sed utper</li><li>Qnde omnis</li><li>Wtusit voluptat</li><li>Rmsantiu</li><li>Gdoloremque</li><li>Wts it olup</li></ul>
  </div>
  <div class="f-col" style="left:720px">
    <h4>Company</h4>
    <ul><li>Home</li><li>Testimonials</li><li>Service</li><li>Certificates</li><li>Contact</li><li>Shop</li></ul>
  </div>
  <div class="f-col newsletter" style="left:853px">
    <h4>Newsletter</h4>
    <div class="field">Name:</div>
    <div class="field">Email:</div>
    <div class="signup">Sign Up</div>
  </div>
  <div class="footer-rule"></div>
  <p class="copyright">© 2017 Velvet Lantern All Copyrights are Reserved.Terms of Use &nbsp; Privacy Policy &nbsp; Sitemap</p>
</footer>

</body>
</html>
```